Vehicle Wrapping Company needs a new look

We need to update our website design. We are the largest fleet vehicle wrapping (installation only - we do not print) company in the US. We do not get much business on this site, we use it mainly to update our portfolio/for new clients to see our capabilities. Looking for something modern and clean. We are the innovators in our industry and the best at what we do, our website should represent that. We haven't updated it for a couple years. Our current website: www.bramblecrestwraps.com
Industry/Entity Type
Advertising
Coding
Coded - Design and coding required
Number of Pages Required
5+ page
Font styles to use
Look and feel
Each slider illustrates characteristics of the customer's brand and the style your logo design should communicate.

```html
<!DOCTYPE html>
<html lang="en">
<head>
<meta charset="utf-8">
<title>Bramblecrest Wraps</title>
<link href="https://fonts.googleapis.com/css2?family=Raleway:wght@500;600;700;800&family=Open+Sans:wght@400;600;700&display=swap" rel="stylesheet">
<style>
:root{
  --orange:#f39a2e;
  --ink:#1d1d1d;
  --grey:#777;
  --black:#0d0d0d;
  --white:#fff;
}
*{box-sizing:border-box;margin:0;padding:0}
html,body{width:1200px;height:2975px;overflow:hidden}
body{font-family:"Open Sans",Arial,sans-serif;color:var(--ink);background:var(--white);position:relative}
.heading{font-family:"Raleway",Arial,sans-serif;font-weight:700;letter-spacing:.5px}
section,header,footer{position:absolute;left:0;width:1200px}
.center{text-align:center}
.rule{width:312px;height:3px;background:var(--orange);margin:16px auto 0}

/* header */
.site-header{top:0;height:105px;border-top:5px solid var(--orange);background:var(--white)}
.brand{position:absolute;left:99px;top:28px;display:flex;align-items:center}
.brand-name{font-family:"Raleway",Arial,sans-serif;font-weight:700;font-size:30px;color:var(--ink);letter-spacing:.5px}
.top-bar{position:absolute;right:98px;top:18px;display:flex;align-items:center;gap:10px;font-size:14px;color:#444}
.social-dot{width:26px;height:26px;border-radius:50%;background:#a9a9a9}
.contact-chip{display:flex;align-items:center;gap:8px;margin-left:22px}
.chip-icon{width:28px;height:28px;border-radius:50%;border:2px solid var(--orange);display:flex;align-items:center;justify-content:center}
.main-nav{position:absolute;right:98px;top:72px;display:flex;gap:30px;font-size:13.5px;font-weight:600;color:#333;letter-spacing:.3px}
.main-nav .active{color:var(--orange)}

/* hero */
.hero{top:105px;height:470px}
.hero-photo{position:absolute;inset:0;background:linear-gradient(100deg,#4e4a46 0%,#8c3a36 30%,#c8242a 48%,#7b7570 70%,#b9b4ab 100%)}
.hero-copy{position:absolute;left:0;right:0;top:130px;text-align:center;color:var(--white)}
.hero-title{font-size:50px;font-weight:800;letter-spacing:1px}
.hero-sub{font-size:19px;line-height:29px;margin-top:8px}
.btn{display:inline-block;background:var(--orange);color:var(--white);font-weight:600;font-size:15px;letter-spacing:.5px}
.hero .btn{margin-top:32px;padding:13px 22px;border:1px solid #fff}
.slide-arrow{position:absolute;top:212px;width:36px;height:50px;background:rgba(0,0,0,.35);display:flex;align-items:center;justify-content:center}

/* welcome */
.welcome{top:575px;height:393px}
.section-title{font-size:31px;padding-top:45px}
.lede{font-size:11.5px;line-height:24px;color:var(--grey);width:820px;margin:28px auto 0}
.services{display:flex;justify-content:space-between;width:1000px;margin:28px auto 0}
.service{width:222px;text-align:center}
.service h3{font-family:"Raleway",Arial,sans-serif;font-size:16px;font-weight:700;margin-top:10px;letter-spacing:.5px}
.service p{font-size:11.5px;line-height:22px;color:var(--grey);margin-top:6px}

/* what we do */
.what-we-do{top:968px;height:476px;background:var(--orange);color:var(--white)}
.what-we-do .rule{background:rgba(255,255,255,.55)}
.what-we-do .lede{color:#fff8ee}
.vehicles{display:grid;grid-template-columns:repeat(4,254px);width:1016px;margin:22px auto 0;row-gap:14px}
.vehicle{text-align:center;height:114px;display:flex;flex-direction:column;align-items:center;justify-content:flex-end}
.vehicle span{font-family:"Raleway",Arial,sans-serif;font-weight:700;font-size:15px;margin-top:10px;letter-spacing:.5px}

/* installs */
.installs{top:1444px;height:546px;background:radial-gradient(circle at 50% 40%,#ffffff 40%,#f2f2f2 100%)}
.installs .section-title{padding-top:44px}
.install-row{position:absolute;left:99px;top:143px;width:1002px;display:flex;justify-content:space-between}
.install{width:317px}
.install-photo{height:208px}
.install h4{font-family:"Raleway",Arial,sans-serif;font-size:16px;font-weight:700;margin-top:22px}
.install p{font-size:11.5px;line-height:22px;color:var(--grey);margin-top:8px;height:66px;overflow:hidden}
.read-more{font-size:11px;font-weight:700;color:var(--orange);margin-top:14px}
.carousel-arrow{position:absolute;top:234px;width:38px;height:38px;border-radius:50%;background:#ddd;display:flex;align-items:center;justify-content:center}

/* call to action */
.cta{top:1990px;height:434px;color:var(--white)}
.cta-photo{position:absolute;inset:0;background:linear-gradient(120deg,#25272a 0%,#3b3e42 45%,#5f6367 65%,#2a2c2f 100%)}
.cta-inner{position:relative;text-align:center}
.cta .section-title{padding-top:44px;font-size:30px}
.cta .rule{width:312px;background:rgba(255,255,255,.45)}
.cta-text{font-size:16px;margin-top:22px}
.cta-actions{display:flex;justify-content:center;align-items:center;gap:26px;margin-top:20px}
.cta .btn{padding:12px 24px}
.cta-or{font-weight:700;font-size:16px}
.cta-phone{display:flex;align-items:center;gap:12px;font-family:"Raleway",Arial,sans-serif;font-weight:700;font-size:26px}
.badges{display:flex;justify-content:space-between;width:1000px;margin:56px auto 0;align-items:center}
.badge{width:146px;height:56px;background:rgba(255,255,255,.85);border-radius:4px}

/* contact */
.contact{top:2424px;height:551px;background:var(--black);color:var(--white)}
.contact .section-title{padding-top:42px;font-size:30px}
.contact .rule{width:312px;background:#444}
.contact-form{position:absolute;left:99px;top:148px;width:630px}
.col-label{font-family:"Raleway",Arial,sans-serif;font-weight:700;font-size:14px;letter-spacing:.3px}
.field-label{font-size:10px;font-weight:600;margin-top:16px;margin-bottom:4px}
.field-row{display:flex;gap:8px}
.field-row .field{flex:1}
.input{background:var(--white);height:32px;width:100%}
.input.tall{height:82px}
.submit{position:absolute;right:0;bottom:-52px;border:2px solid var(--white);padding:8px 18px;font-size:12px;font-weight:700}
.contact-info{position:absolute;left:809px;top:148px;width:300px}
.info-item{display:flex;align-items:center;gap:20px;margin-top:22px;font-size:15px;line-height:22px}
.info-icon{width:36px;height:36px;border-radius:50%;border:2px solid var(--white);display:flex;align-items:center;justify-content:center;flex:none}
.social-row{display:flex;gap:12px;margin-top:16px}
.social-square{width:24px;height:24px;background:var(--white);border-radius:3px}
.site-footer{top:2908px;height:67px;border-top:1px solid #2a2a2a;background:var(--black);color:#bbb;font-size:11px;text-align:center;padding-top:22px;width:1002px;left:99px}
</style>
</head>
<body>

<header class="site-header">
  <div class="brand">
    <div class="brand-name">BRAMBLECREST WRAPS</div>
  </div>
  <div class="top-bar">
    <div class="social-dot"></div><div class="social-dot"></div><div class="social-dot"></div><div class="social-dot"></div>
    <div class="contact-chip">
      <div class="chip-icon"><svg width="14" height="14" viewBox="0 0 24 24"><path fill="#f39a2e" d="M6.6 10.8a15 15 0 0 0 6.6 6.6l2.2-2.2a1 1 0 0 1 1-.25 11.4 11.4 0 0 0 3.6.57 1 1 0 0 1 1 1V20a1 1 0 0 1-1 1A17 17 0 0 1 3 4a1 1 0 0 1 1-1h3.5a1 1 0 0 1 1 1c0 1.25.2 2.45.57 3.57a1 1 0 0 1-.25 1z"/></svg></div>
      555-014-2290
    </div>
    <div class="contact-chip">
      <div class="chip-icon"><svg width="14" height="12" viewBox="0 0 24 18"><rect x="1" y="1" width="22" height="16" rx="2" fill="none" stroke="#f39a2e" stroke-width="2.5"/><path d="M2 2l10 8 10-8" fill="none" stroke="#f39a2e" stroke-width="2.5"/></svg></div>
      info@bramblecrestwraps.com
    </div>
  </div>
  <nav class="main-nav">
    <span class="active">HOME</span><span>ABOUT</span><span>PROJECTS</span><span>PORTFOLIO</span><span>PRESS</span><span>CONTACT</span>
    <svg width="14" height="14" viewBox="0 0 24 24"><circle cx="10" cy="10" r="7" fill="none" stroke="#333" stroke-width="3"/><path d="M15 15l7 7" stroke="#333" stroke-width="3"/></svg>
  </nav>
</header>

<section class="hero">
  <div class="hero-photo" role="img" aria-label="Red sports car with a freshly installed wrap parked on a city street beside a graffiti wall"></div>
  <div class="slide-arrow" style="left:56px"><svg width="12" height="20" viewBox="0 0 12 20"><path d="M10 2L2 10l8 8" fill="none" stroke="#fff" stroke-width="3"/></svg></div>
  <div class="slide-arrow" style="right:56px"><svg width="12" height="20" viewBox="0 0 12 20"><path d="M2 2l8 8-8 8" fill="none" stroke="#fff" stroke-width="3"/></svg></div>
  <div class="hero-copy">
    <h1 class="hero-title heading">AFFORDABLE . DURABLE . MOBILE</h1>
    <p class="hero-sub">Our main focus is providing the client with our highest standard of wrapping so<br>your graphics will adhere to their intended lifetime and warranty.</p>
    <span class="btn">REQUEST A QUOTE</span>
  </div>
</section>

<section class="welcome center">
  <h2 class="section-title heading">WELCOME TO BRAMBLECREST WRAPS</h2>
  <div class="rule"></div>
  <p class="lede">Vehicle wraps are being used by companies and car owners to showcase their attention-grabbing designs, campaigns or company logo(s) with the sole purpose of delivering their messages to the masses. Whether on the road or sailing the high seas.</p>
  <div class="services">
    <div class="service">
      <svg width="52" height="48" viewBox="0 0 52 48"><rect x="4" y="8" width="36" height="36" rx="5" fill="none" stroke="#f39a2e" stroke-width="3.5"/><path d="M20 30l2-8L42 2l6 6-20 20z" fill="#f39a2e"/></svg>
      <h3>DESIGN</h3><p>As a graphic installation company, our main focus is providing the client with our highest standard</p>
    </div>
    <div class="service">
      <svg width="48" height="48" viewBox="0 0 48 48"><path d="M40 20A17 17 0 0 0 9 14" fill="none" stroke="#f39a2e" stroke-width="5"/><path d="M4 6v12h12z" fill="#f39a2e"/><path d="M8 28a17 17 0 0 0 31 6" fill="none" stroke="#f39a2e" stroke-width="5"/><path d="M44 42V30H32z" fill="#f39a2e"/></svg>
      <h3>RESTYLING</h3><p>As a graphic installation company, our main focus is providing the client with our highest standard</p>
    </div>
    <div class="service">
      <svg width="52" height="48" viewBox="0 0 52 46"><rect x="3" y="3" width="46" height="40" rx="3" fill="none" stroke="#f39a2e" stroke-width="4"/><circle cx="16" cy="15" r="5" fill="#f39a2e"/><path d="M8 37l12-12 6 6 10-12 10 18z" fill="#f39a2e"/></svg>
      <h3>WRAPPING</h3><p>As a graphic installation company, our main focus is providing the client with our highest standard</p>
    </div>
    <div class="service">
      <svg width="48" height="48" viewBox="0 0 48 48"><path d="M6 42l20-20" stroke="#f39a2e" stroke-width="7" stroke-linecap="round"/><path d="M24 16a12 12 0 0 1 16-12l-8 8 2 6 6 2 8-8a12 12 0 0 1-12 16z" fill="#f39a2e"/></svg>
      <h3>MAINTENANCE</h3><p>As a graphic installation company, our main focus is providing the client with our highest standard</p>
    </div>
  </div>
</section>

<section class="what-we-do center">
  <h2 class="section-title heading">WHAT WE DO</h2>
  <div class="rule"></div>
  <p class="lede">Vehicle wraps are being used by companies and car owners to showcase their attention-grabbing designs, campaigns or company logo(s) with the sole purpose of delivering their messages to the masses. Whether on the road or sailing the high seas.</p>
  <div class="vehicles">
    <div class="vehicle"><svg width="124" height="60" viewBox="0 0 124 60"><rect x="4" y="4" width="116" height="42" rx="8" fill="#fff"/><rect x="12" y="12" width="18" height="14" fill="#f39a2e"/><rect x="36" y="12" width="18" height="14" fill="#f39a2e"/><rect x="60" y="12" width="18" height="14" fill="#f39a2e"/><rect x="84" y="12" width="28" height="14" fill="#f39a2e"/><circle cx="28" cy="48" r="9" fill="#fff" stroke="#f39a2e" stroke-width="3"/><circle cx="96" cy="48" r="9" fill="#fff" stroke="#f39a2e" stroke-width="3"/></svg><span>BUSES</span></div>
    <div class="vehicle"><svg width="144" height="60" viewBox="0 0 144 60"><path d="M6 44V32q0-8 10-10l20-4 18-14h40l24 16q18 2 20 12v12z" fill="#fff"/><path d="M58 10h14v12H44zM78 10h14l14 12H78z" fill="#f39a2e"/><path d="M72 28l-8 10h8l-6 10" stroke="#f39a2e" stroke-width="3" fill="none"/><circle cx="36" cy="46" r="10" fill="#fff" stroke="#f39a2e" stroke-width="3"/><circle cx="112" cy="46" r="10" fill="#fff" stroke="#f39a2e" stroke-width="3"/></svg><span>CARS</span></div>
    <div class="vehicle"><svg width="134" height="60" viewBox="0 0 134 60"><rect x="4" y="8" width="82" height="32" rx="14" fill="#fff"/><rect x="22" y="2" width="12" height="8" fill="#fff"/><path d="M92 12h24l14 16v16H92z" fill="#fff"/><rect x="98" y="17" width="16" height="10" fill="#f39a2e"/><rect x="4" y="40" width="126" height="6" fill="#fff"/><circle cx="24" cy="48" r="9" fill="#fff" stroke="#f39a2e" stroke-width="3"/><circle cx="110" cy="48" r="9" fill="#fff" stroke="#f39a2e" stroke-width="3"/></svg><span>TANKERS</span></div>
    <div class="vehicle"><svg width="134" height="60" viewBox="0 0 134 60"><path d="M4 46V10q0-6 6-6h72q8 0 14 8l14 14q20 4 20 14v6z" fill="#fff"/><path d="M84 10h10l14 16H84z" fill="#f39a2e"/><circle cx="30" cy="46" r="10" fill="#fff" stroke="#f39a2e" stroke-width="3"/><circle cx="104" cy="46" r="10" fill="#fff" stroke="#f39a2e" stroke-width="3"/></svg><span>VANS</span></div>
    <div class="vehicle"><svg width="140" height="60" viewBox="0 0 140 60"><rect x="4" y="2" width="92" height="40" fill="#fff"/><path d="M100 14h22l14 14v14h-36z" fill="#fff"/><rect x="106" y="19" width="14" height="10" fill="#f39a2e"/><circle cx="26" cy="48" r="9" fill="#fff" stroke="#f39a2e" stroke-width="3"/><circle cx="66" cy="48" r="9" fill="#fff" stroke="#f39a2e" stroke-width="3"/><circle cx="118" cy="48" r="9" fill="#fff" stroke="#f39a2e" stroke-width="3"/></svg><span>TRAILERS</span></div>
    <div class="vehicle"><svg width="140" height="60" viewBox="0 0 140 60"><path d="M4 18h30l12-16h30v40H4z" fill="#fff"/><rect x="80" y="2" width="56" height="40" fill="#fff"/><path d="M36 18l10-12h20v12z" fill="#f39a2e"/><circle cx="26" cy="48" r="9" fill="#fff" stroke="#f39a2e" stroke-width="3"/><circle cx="110" cy="48" r="9" fill="#fff" stroke="#f39a2e" stroke-width="3"/></svg><span>TRUCKS</span></div>
    <div class="vehicle"><svg width="84" height="76" viewBox="0 0 84 76"><path d="M4 4h76v14H4z" fill="#fff"/><path d="M4 18h76l-4 10H8z" fill="#fff"/><rect x="10" y="30" width="64" height="44" fill="#fff"/><rect x="18" y="38" width="22" height="20" fill="#f39a2e"/><rect x="48" y="38" width="18" height="36" fill="#f39a2e"/></svg><span>RETAILS</span></div>
    <div class="vehicle"><svg width="84" height="80" viewBox="0 0 84 80"><path d="M8 4h52q20 2 20 24v22H8z" fill="#fff"/><rect x="4" y="50" width="80" height="10" fill="#fff"/><path d="M12 50V34h64v16" fill="#f39a2e"/><path d="M18 34v16M26 34v16M34 34v16M42 34v16M50 34v16M58 34v16M66 34v16" stroke="#fff" stroke-width="3"/><rect x="10" y="60" width="6" height="18" fill="#fff"/><rect x="70" y="60" width="6" height="18" fill="#fff"/></svg><span>SPECIALITY</span></div>
  </div>
</section>

<section class="installs">
  <div class="center">
    <h2 class="section-title heading">A FEW OF OUR LATEST INSTALLS</h2>
    <div class="rule" style="width:630px"></div>
  </div>
  <div class="carousel-arrow" style="left:50px"><svg width="10" height="14" viewBox="0 0 10 14"><path d="M8 1L2 7l6 6" fill="none" stroke="#888" stroke-width="2"/></svg></div>
  <div class="carousel-arrow" style="right:56px"><svg width="10" height="14" viewBox="0 0 10 14"><path d="M2 1l6 6-6 6" fill="none" stroke="#888" stroke-width="2"/></svg></div>
  <div class="install-row">
    <article class="install">
      <div class="install-photo" role="img" aria-label="Row of stainless steel fuel tankers wrapped in bright food graphics" style="background:linear-gradient(160deg,#3d5a8a 0%,#6d7e9a 35%,#c4343a 60%,#e2b04a 100%)"></div>
      <h4>COASTWAY FUEL</h4>
      <p>Bramblecrest Wraps was selected by Coastway Fuel Co. to fully wrap a series of stainless steel tankers (including the "white" tractors) to promote …</p>
      <div class="read-more">READ MORE &gt;&gt;</div>
    </article>
    <article class="install">
      <div class="install-photo" role="img" aria-label="Red compact hybrid car wrapped with a bakery promotion in a parking lot" style="background:linear-gradient(160deg,#5a6256 0%,#8a1f24 45%,#c8383c 65%,#707470 100%)"></div>
      <h4>SHE'S MY CHERRY PIE</h4>
      <p>Old flame lost her spark? Bramblecrest Wraps transforms this 1950s Halvern Business Coupe from '9 to 5' to dinner and drinks by restoring this hot rod.</p>
      <div class="read-more">READ MORE &gt;&gt;</div>
    </article>
    <article class="install">
      <div class="install-photo" role="img" aria-label="Grand piano wrapped in glossy bright blue on a dark stage" style="background:radial-gradient(circle at 45% 55%,#3aa7e8 0%,#1d5f9a 35%,#111 80%)"></div>
      <h4>2014 MUSICAL INSTRUMENT WRAPS</h4>
      <p>We had another memorable year wrapping instruments for high-profile musicians at various televised events, from the Silver Chord Awards to Open Stage Tonight.</p>
      <div class="read-more">READ MORE &gt;&gt;</div>
    </article>
  </div>
</section>

<section class="cta">
  <div class="cta-photo" role="img" aria-label="White muscle car with dark blue racing stripes"></div>
  <div class="cta-inner">
    <h2 class="section-title heading">NEED YOUR VEHICLE WRAPPED?</h2>
    <div class="rule"></div>
    <p class="cta-text">Get in touch with us today via the Contact page or by calling us</p>
    <div class="cta-actions">
      <span class="btn">CONTACT US TODAY</span>
      <span class="cta-or">OR</span>
      <span class="cta-phone"><svg width="22" height="22" viewBox="0 0 24 24"><path fill="#fff" d="M6.6 10.8a15 15 0 0 0 6.6 6.6l2.2-2.2a1 1 0 0 1 1-.25 11.4 11.4 0 0 0 3.6.57 1 1 0 0 1 1 1V20a1 1 0 0 1-1 1A17 17 0 0 1 3 4a1 1 0 0 1 1-1h3.5a1 1 0 0 1 1 1c0 1.25.2 2.45.57 3.57a1 1 0 0 1-.25 1z"/></svg>555-014-2290</span>
    </div>
    <div class="badges">
      <div class="badge"></div><div class="badge"></div><div class="badge"></div><div class="badge" style="width:200px"></div><div class="badge"></div>
    </div>
  </div>
</section>

<section class="contact">
  <div class="center">
    <h2 class="section-title heading">CONTACT US</h2>
    <div class="rule"></div>
  </div>
  <div class="contact-form">
    <div class="col-label">CONTACT FORM</div>
    <div class="field-row">
      <div class="field"><div class="field-label">NAME :</div><div class="input"></div></div>
      <div class="field"><div class="field-label">PHONE :</div><div class="input"></div></div>
    </div>
    <div class="field-label">EMAIL :</div><div class="input"></div>
    <div class="field-label">MESSAGE :</div><div class="input tall"></div>
    <div class="submit">SUBMIT</div>
  </div>
  <div class="contact-info">
    <div class="col-label">CONTACT INFORMATION</div>
    <div class="info-item"><div class="info-icon"><svg width="14" height="18" viewBox="0 0 14 18"><path d="M7 0a7 7 0 0 1 7 7c0 5-7 11-7 11S0 12 0 7a7 7 0 0 1 7-7z" fill="#fff"/><circle cx="7" cy="7" r="2.5" fill="#0d0d0d"/></svg></div><span style="font-size:13px">1820 Harbor Line Drive, Suite 304<br>Tampa, FL 33602</span></div>
    <div class="info-item"><div class="info-icon"><svg width="16" height="12" viewBox="0 0 24 18"><rect x="1" y="1" width="22" height="16" rx="2" fill="#fff"/><path d="M2 2l10 8 10-8" fill="none" stroke="#0d0d0d" stroke-width="2"/></svg></div>info@bramblecrestwraps.com</div>
    <div class="info-item"><div class="info-icon"><svg width="14" height="14" viewBox="0 0 24 24"><path fill="#fff" d="M6.6 10.8a15 15 0 0 0 6.6 6.6l2.2-2.2a1 1 0 0 1 1-.25 11.4 11.4 0 0 0 3.6.57 1 1 0 0 1 1 1V20a1 1 0 0 1-1 1A17 17 0 0 1 3 4a1 1 0 0 1 1-1h3.5a1 1 0 0 1 1 1c0 1.25.2 2.45.57 3.57a1 1 0 0 1-.25 1z"/></svg></div>555-014-2290</div>
    <div class="col-label" style="margin-top:24px">SOCIAL</div>
    <div class="social-row"><div class="social-square"></div><div class="social-square"></div><div class="social-square"></div><div class="social-square"></div><div class="social-square"></div></div>
  </div>
</section>

<footer class="site-footer">Copyright © 2016, Bramblecrest Wraps. All Rights Reserved.</footer>

</body>
</html>
```